Dozing Heron

Need a business card for our restaurant. Restaurant and Bar in the mountains of North Idaho. Rustic looking card

Contact Information for Business Card

rustic design, wood and metal looking, primarily neutral colors

Requirements
Must have
• Name, address, phone number, website, email address

```html
<!DOCTYPE html>
<html lang="en">
<head>
<meta charset="utf-8">
<title>Dozing Heron – Business Card</title>
<link href="https://fonts.googleapis.com/css2?family=Montserrat:wght@400;500;700&display=swap" rel="stylesheet">
<style>
  :root {
    --page: #e6e4e0;
    --card-white: #ffffff;
    --card-black: #232323;
    --ink: #1c1c1c;
    --gold: #c6a25c;
    --white: #ffffff;
  }
  html, body {
    margin: 0;
    padding: 0;
    width: 1200px;
    height: 1200px;
    overflow: hidden;
    background: var(--page);
    font-family: "Montserrat", Arial, sans-serif;
  }
  .canvas {
    position: relative;
    width: 1200px;
    height: 1200px;
  }
  .card {
    position: absolute;
    left: 145px;
    width: 910px;
    height: 520px;
    border-radius: 40px;
    overflow: hidden;
    box-shadow: 0 8px 24px rgba(0,0,0,0.18);
  }
  .card-front { top: 50px; background: var(--card-white); }
  .card-back  { top: 630px; background: var(--card-black); border: 2px solid var(--gold); box-sizing: border-box; }
  .wave { position: absolute; inset: 0; width: 100%; height: 100%; }
  .identity {
    position: absolute;
    left: 70px;
    top: 200px;
  }
  .full-name {
    margin: 0;
    font-size: 48px;
    font-weight: 700;
    color: var(--gold);
    letter-spacing: 0.5px;
    line-height: 1.05;
  }
  .job-title {
    margin: 2px 0 22px;
    font-size: 36px;
    font-weight: 400;
    color: var(--ink);
    line-height: 1.1;
  }
  .contact-list { list-style: none; margin: 0; padding: 0; }
  .contact-list li {
    display: flex;
    align-items: flex-start;
    gap: 14px;
    font-size: 23px;
    color: var(--ink);
    line-height: 30px;
  }
  .contact-list svg { flex: none; width: 24px; height: 24px; margin-top: 3px; fill: var(--gold); }
  .brand-name {
    position: absolute;
    margin: 0;
    font-weight: 500;
    letter-spacing: 4px;
    text-transform: uppercase;
    text-align: center;
    white-space: nowrap;
  }
  .card-front .brand-name { right: 80px; top: 150px; font-size: 34px; color: var(--ink); }
  .card-back .brand-name { left: 0; right: 0; top: 235px; font-size: 46px; color: var(--white); }
</style>
</head>
<body>
<main class="canvas">
  <section class="card card-front">
    <svg class="wave" viewBox="0 0 910 520" preserveAspectRatio="none" aria-hidden="true">
      <path d="M300,520 C380,380 560,410 700,345 C800,300 850,220 910,200 L910,520 Z" fill="var(--gold)"/>
      <path d="M335,520 C410,400 575,425 712,362 C810,318 860,250 910,232 L910,520 Z" fill="var(--white)"/>
      <path d="M350,520 C425,410 585,432 720,372 C815,330 865,265 910,250 L910,520 Z" fill="var(--card-black)"/>
    </svg>
    <p class="brand-name">Dozing Heron</p>
    <div class="identity">
      <h1 class="full-name">FULL NAME</h1>
      <p class="job-title">TITLE</p>
      <ul class="contact-list">
        <li><svg viewBox="0 0 24 24"><path d="M6.6 10.8a15 15 0 0 0 6.6 6.6l2.2-2.2a1 1 0 0 1 1-.25 11.4 11.4 0 0 0 3.6.57 1 1 0 0 1 1 1V20a1 1 0 0 1-1 1A17 17 0 0 1 3 4a1 1 0 0 1 1-1h3.5a1 1 0 0 1 1 1c0 1.25.2 2.45.57 3.57a1 1 0 0 1-.25 1z"/></svg>(000) 000 0000</li>
        <li><svg viewBox="0 0 24 24"><path d="M2 5h20v14H2z M2 5l10 8 10-8" fill="none" stroke="var(--gold)" stroke-width="2.4"/></svg>email@company.com</li>
        <li><svg viewBox="0 0 24 24"><g fill="none" stroke="var(--gold)" stroke-width="1.8"><circle cx="12" cy="12" r="10"/><ellipse cx="12" cy="12" rx="4.5" ry="10"/><path d="M2 12h20M4 7h16M4 17h16"/></g></svg>www.company.com</li>
        <li><svg viewBox="0 0 24 24"><path d="M12 2a7 7 0 0 0-7 7c0 5 7 13 7 13s7-8 7-13a7 7 0 0 0-7-7zm0 9.5A2.5 2.5 0 1 1 12 6.5a2.5 2.5 0 0 1 0 5z"/></svg>123 Name Street, 000<br>Your City, 00000-000</li>
      </ul>
    </div>
  </section>

  <section class="card card-back">
    <p class="brand-name">Dozing Heron</p>
  </section>
</main>
</body>
</html>
```